Simple 3 page web design project

This is a simple 3 or 4 page site that is very straight forward.

I have a furnished apartment to lease, and wish to design a clean 3 or 4 page website to advertise the apartment. I am thinking a clean black background with a nice image of the inside of the apartment in the center of the page.

I have attached a rough mockup I did to show what I was thinking of.

Also, room for a nice title and some text above the large picture. At the bottom or on the side, there should be thumbnails that can be clicked to view other images of the apartment with labels below each one.

A menu "Home", "how to rent", and "contact" should be included, as well as a map of where the apartment is on the last page.

I prefer the project be written in HTML5.

I will provide the address and the pictures when I decide on a provider.

I have attached a sample website mock up I did in photoshop to give you an idea of what I am looking for.

Target Market(s)

business travelers and families needing temporary homes

Industry/Entity Type

Apartment

Requirements
Must have
• Should be written in HTML5
Must be able to upload and resize images using thumbnails
must have a contact form
must have the address on a google map on one of the pages
Must have normal items to optomize google search, such as title page, title, etc.
Should not have
• No add-in modules that will have to be kept up. The site shold be written in HTML

```html
<!DOCTYPE html>
<html lang="en">
<head>
<meta charset="utf-8">
<title>Furnished Executive Apartment // Mobile, AL</title>
<meta name="description" content="Newly renovated and furnished executive apartment for lease in Mobile, AL.">
<link rel="stylesheet" href="https://fonts.googleapis.com/css2?family=Arimo:wght@400;700&family=Inter:wght@200&display=swap">
<style>
  :root {
    --page-bg: #1d1d1d;
    --side-band: #252525;
    --side-type: #5a5a5a;
    --gold: #c5a22c;
    --white: #ffffff;
    --muted: #6f6f6f;
    --rule: #d8d8d8;
    --caption-bg: rgba(20, 20, 20, 0.82);
  }
  * { box-sizing: border-box; margin: 0; padding: 0; }
  html, body {
    width: 1200px; height: 956px; overflow: hidden;
    background: var(--page-bg);
    font-family: "Arimo", Helvetica, Arial, sans-serif;
    color: var(--white);
  }
  .page { position: relative; width: 1200px; height: 956px; }

  .brand-band {
    position: absolute; left: 965px; top: 0; width: 140px; height: 956px;
    background: var(--side-band);
  }
  .brand-band__name {
    position: absolute; left: 1040px; top: 24px;
    writing-mode: vertical-rl;
    font-family: "Arimo", Helvetica, Arial, sans-serif;
    font-weight: 400;
    font-size: 30px; line-height: 36px; letter-spacing: 2px;
    color: var(--side-type);
    white-space: nowrap;
  }

  .site-title {
    position: absolute; left: 0; width: 1200px; top: 42px;
    text-align: center; font-size: 29px; line-height: 40px;
    color: var(--gold); font-weight: 700;
  }
  .site-title__place {
    font-family: "Inter", Helvetica, sans-serif; font-weight: 200;
  }

  .main-nav {
    position: absolute; left: 460px; top: 103px; width: 281px; height: 29px;
    border-top: 1px solid var(--rule); border-bottom: 1px solid var(--rule);
    display: flex; justify-content: space-between; align-items: center;
    padding: 0 10px;
  }
  .main-nav a {
    color: var(--white); text-decoration: none; font-size: 15px;
  }

  .hero {
    position: absolute; left: 190px; top: 157px; width: 820px; height: 400px;
    background: linear-gradient(100deg, #d9d9d9 0%, #8f8f8f 38%, #7a7a7a 55%, #b33a32 70%, #e8e8e8 100%);
  }
  .hero__caption {
    position: absolute; left: 0; bottom: 0; width: 100%; height: 45px;
    background: var(--caption-bg);
    color: var(--gold); font-size: 18px; line-height: 48px; text-align: center;
  }

  .thumbs {
    position: absolute; left: 190px; top: 567px; width: 820px; height: 76px;
    display: flex; gap: 6.8px; list-style: none;
  }
  .thumbs li {
    width: 75.8px; height: 76px;
    background: linear-gradient(135deg, #e6e6e6, #8a8a8a);
  }
  .thumbs li:nth-child(1) { background: linear-gradient(135deg, #bdbdbd, #b33a32); border: 1px solid var(--gold); }
  .thumbs li:nth-child(2) { background: linear-gradient(135deg, #d8d8d8, #2a2a2a); }
  .thumbs li:nth-child(3) { background: linear-gradient(135deg, #f0f0f0, #a09585); }
  .thumbs li:nth-child(4) { background: linear-gradient(135deg, #c7c2bb, #3a3a3a); }
  .thumbs li:nth-child(5) { background: linear-gradient(135deg, #f4f4f4, #6e6e6e); }
  .thumbs li:nth-child(6) { background: linear-gradient(135deg, #9a9a8a, #e8e8e0); }
  .thumbs li:nth-child(7) { background: linear-gradient(135deg, #2a2a2a, #d0d0d0); }
  .thumbs li:nth-child(8) { background: linear-gradient(135deg, #e0e0e0, #3a3a3a); }
  .thumbs li:nth-child(9) { background: linear-gradient(135deg, #e8e4d8, #222222); }
  .thumbs li:nth-child(10) { background: linear-gradient(135deg, #d8cfc0, #4a4038); }

  .intro { position: absolute; left: 190px; top: 686px; width: 822px; }
  .intro__heading { font-size: 24px; line-height: 32px; font-weight: 700; }
  .intro__text { margin-top: 12px; font-size: 14.4px; line-height: 24px; letter-spacing: 0.12px; }

  .site-footer {
    position: absolute; left: 0; top: 894px; width: 1200px; text-align: center;
  }
  .site-footer__copy { font-size: 11px; line-height: 14px; color: var(--muted); }
  .share-links { margin-top: 7px; display: flex; justify-content: center; gap: 4px; padding-left: 26px; }
</style>
</head>
<body>
<div class="page">
  <aside class="brand-band"></aside>
  <div class="brand-band__name">Bayou Crest Properties</div>

  <header>
    <h1 class="site-title">Furnished Executive Apartment <span class="site-title__place">// Mobile, AL</span></h1>
    <nav class="main-nav">
      <a href="#">Welcome</a>
      <a href="#">How to Rent</a>
      <a href="#">Contact</a>
    </nav>
  </header>

  <main>
    <figure class="hero" role="img" aria-label="Photo of the apartment living room with a red sectional sofa, white cabinetry and dining table">
      <figcaption class="hero__caption">Newly Renovated and Furnished Executive Apartment</figcaption>
    </figure>

    <ul class="thumbs">
      <li role="img" aria-label="Thumbnail: living room with red sofa"></li>
      <li role="img" aria-label="Thumbnail: kitchen with round island"></li>
      <li role="img" aria-label="Thumbnail: bright sitting area"></li>
      <li role="img" aria-label="Thumbnail: lounge with rug"></li>
      <li role="img" aria-label="Thumbnail: white sofa and coffee table"></li>
      <li role="img" aria-label="Thumbnail: corner sofa"></li>
      <li role="img" aria-label="Thumbnail: bedroom"></li>
      <li role="img" aria-label="Thumbnail: media wall"></li>
      <li role="img" aria-label="Thumbnail: modern lounge chair"></li>
      <li role="img" aria-label="Thumbnail: neutral living room"></li>
    </ul>

    <section class="intro">
      <h2 class="intro__heading">Furnished Executive Apartment</h2>
      <p class="intro__text">Lorem ipsum dolor sit amet, consectetur adipiscing elit. Vestibulum porttitor ligula non metus commodo ultrices. Curabitur elementum libero eget lacus lobortis gravida. Mauris sem ante, scelerisque a aliquam vitae, commodo at eros. Donec suscipit sagittis ultricies. Fusce vitae mi risus. Praesent diam nunc, vestibulum lobortis lobortis a, viverra et nunc. Cras ornare nibh<br>vitae diam luctus at iaculis tortor lacinia. Phasellus id blandit leo. Nunc fringilla, arcu sit amet ullamcorper vulputate, nulla<br>diam auctor tellus, et tempus justo purus eget odio. Duis eget neque ac urna semper tincidunt a em eget nibh ni u elit.</p>
    </section>
  </main>

  <footer class="site-footer">
    <p class="site-footer__copy">Copyright © 2013 Bayou Crest Group, LLC.</p>
    <div class="share-links">
      <svg width="16" height="16" role="img" aria-label="Share link"><rect width="16" height="16" rx="2" fill="#4a5f8c"/></svg>
      <svg width="16" height="16" role="img" aria-label="Share link"><rect width="16" height="16" rx="2" fill="#4aa3d4"/></svg>
      <svg width="16" height="16" role="img" aria-label="Share by email"><rect width="16" height="16" rx="2" fill="#e6e6e6"/></svg>
      <svg width="16" height="16" role="img" aria-label="Share link"><rect width="16" height="16" rx="2" fill="#c0262d"/></svg>
      <svg width="16" height="16" role="img" aria-label="More sharing options"><rect width="16" height="16" rx="2" fill="#e8643a"/></svg>
    </div>
  </footer>
</div>
</body>
</html>
```